AV & Engineering company needs a Business Card Design

Like the simple design, don't too colorful. Smart & professional feel

Industry/Entity Type

Business

Requirements
Nice to have
• I would like to see the vertical design.

```html
<!DOCTYPE html>
<html lang="en">
<head>
<meta charset="utf-8">
<title>Veltar Systems – Business Card Options</title>
<link href="https://fonts.googleapis.com/css2?family=Open+Sans:wght@400;600;700;800&display=swap" rel="stylesheet">
<style>
  :root {
    --brand-red: #9e1d22;
    --ink: #1a1a1a;
    --muted: #6b6b6b;
    --paper: #ffffff;
    --bg-light: #ffffff;
    --bg-dark: #cfcfd1;
    --tint: #f6e9e7;
  }
  * { box-sizing: border-box; margin: 0; padding: 0; }
  html, body { width: 1200px; height: 843px; overflow: hidden; }
  body {
    font-family: "Open Sans", Arial, sans-serif;
    background: linear-gradient(160deg, var(--bg-light) 0%, #f1f1f2 45%, var(--bg-dark) 100%);
    position: relative;
  }
  .option-label {
    position: absolute;
    font-size: 17px;
    font-weight: 600;
    letter-spacing: 1px;
    color: var(--ink);
  }
  .option-label--one { left: 138px; top: 286px; }
  .option-label--two { left: 598px; top: 98px; }
  .option-label--front { left: 515px; top: 690px; font-weight: 400; }

  .card {
    position: absolute;
    width: 440px;
    height: 252px;
    box-shadow: 0 14px 30px rgba(0,0,0,0.18);
    overflow: hidden;
  }
  .card--back-red { left: 138px; top: 320px; background: var(--brand-red); }
  .card--back-white { left: 640px; top: 132px; background: var(--paper); }
  .card--front { left: 680px; top: 520px; background: var(--paper); }

  .wordmark {
    position: absolute;
    display: flex;
    align-items: center;
    gap: 12px;
    font-weight: 800;
    text-transform: uppercase;
    letter-spacing: 0.5px;
    line-height: 1.1;
  }
  .wordmark__square { width: 30px; height: 30px; flex: none; }
  .wordmark__name { font-size: 22px; }
  .wordmark__name span { display: block; }

  .card--back-red .wordmark { left: 50%; top: 50%; transform: translate(-50%, -50%); color: var(--paper); }
  .card--back-red .wordmark__square { background: var(--paper); }
  .card--back-white .wordmark { left: 50%; top: 50%; transform: translate(-50%, -50%); color: var(--brand-red); }
  .card--back-white .wordmark__square { background: var(--brand-red); }

  .card--front .wordmark { right: 26px; top: 24px; color: var(--brand-red); gap: 8px; }
  .card--front .wordmark__square { width: 18px; height: 18px; background: var(--brand-red); }
  .card--front .wordmark__name { font-size: 13px; }

  .front-decor {
    position: absolute;
    right: -40px;
    bottom: -60px;
    width: 220px;
    height: 220px;
    border-radius: 50%;
    background: var(--tint);
  }
  .holder { position: absolute; left: 28px; top: 92px; }
  .holder__name { font-size: 17px; font-weight: 700; color: var(--brand-red); line-height: 1.1; }
  .holder__role { font-size: 9px; color: var(--muted); }
  .contact {
    position: absolute;
    left: 28px;
    top: 150px;
    font-size: 10.5px;
    color: var(--brand-red);
    line-height: 1.25;
  }
  .contact p + p { margin-top: 7px; }
  .contact small { font-size: 8px; }
</style>
</head>
<body>
  <p class="option-label option-label--one">Back side option 1</p>
  <p class="option-label option-label--two">Back side option 2</p>
  <p class="option-label option-label--front">front side</p>

  <section class="card card--back-red" aria-label="Back side option 1">
    <div class="wordmark">
      <span class="wordmark__square"></span>
      <span class="wordmark__name"><span>Veltar Systems</span><span>Company Ltd</span></span>
    </div>
  </section>

  <section class="card card--back-white" aria-label="Back side option 2">
    <div class="wordmark">
      <span class="wordmark__square"></span>
      <span class="wordmark__name"><span>Veltar Systems</span><span>Company Ltd</span></span>
    </div>
  </section>

  <section class="card card--front" aria-label="Front side">
    <div class="front-decor"></div>
    <div class="wordmark">
      <span class="wordmark__square"></span>
      <span class="wordmark__name"><span>Veltar Systems</span><span>Company Ltd</span></span>
    </div>
    <div class="holder">
      <p class="holder__name">YOUR NAME</p>
      <p class="holder__role">designation</p>
    </div>
    <div class="contact">
      <p>address line 1<br>city 55555</p>
      <p>+1.999.999.9999 <small>(mobile)</small><br>+1.888.888.8888 <small>(facsimile)</small></p>
      <p>emailid@website.com<br>www.website.com</p>
    </div>
  </section>
</body>
</html>
```